illustration of the importance of using your money as voting power for the environment

Illustration to read either per word, or creative interpretation (open to suggestions) " Vote, use your $ to vote for your favourite candidate" and then below it will have two choices the first reading "Berries- imported (yes), regulated (questionable), Free trade over Free Health (absolutely)" second choice reading "Berries- local (yes), organic (hopefully), regulated (most definatley) Free trade over Free Health (not on Australia's watch). there will be a little thought bubble next to the second choice that says "I know we cost more, but do you think people will get it yet?). It must have my logo on the bottom. I have uploaded the file.

The project is about using your money or your wallet to make a choice, making that choice is equal to voting. Every time you buy something, you are voting for a 'good' project, one that is environmentally friendly and gives positvely to the environment OR you are voting/buying a 'bad' product that is unsustainable, potentially poisonous and damages people and the environment. We just had a health scare here becuase of imported berries that were not regulated because of our new free trade agreement with china, although this is not about china, its about be aware as a consumer and making or Voting for your future.

Target Market(s)

20's- 50's

Industry/Entity Type

Environment

Requirements
Must have
• my logo and business name

```html
<!DOCTYPE html>
<html lang="en">
<head>
<meta charset="utf-8">
<title>Vote With Your Dollar – Berries</title>
<link rel="stylesheet" href="https://fonts.googleapis.com/css2?family=Source+Sans+3:wght@400;600&display=swap">
<style>
  :root {
    --bg: #1b5a3c;
    --bg-soft: #25664a;
    --ribbon: #ef5150;
    --ribbon-shade: #c93c3c;
    --gold: #f7c243;
    --beige: #cfc7ae;
    --bubble: #f6bb2b;
    --bubble-text: #e8455a;
    --white: #ffffff;
  }
  * { margin: 0; padding: 0; box-sizing: border-box; }
  html, body { width: 1200px; height: 1002px; overflow: hidden; background: var(--bg); }
  .canvas {
    position: relative;
    width: 1200px;
    height: 1002px;
    background: var(--bg);
    font-family: "Source Sans 3", "Myriad Pro", sans-serif;
    overflow: hidden;
  }
  .world-map {
    position: absolute;
    left: 165px; top: 405px;
    width: 840px; height: 300px;
    border-radius: 120px;
    background: radial-gradient(ellipse at center, rgba(70,120,90,0.35), rgba(27,90,60,0) 70%);
  }
  .artwork { position: absolute; left: 0; top: 0; }
  .label { position: absolute; white-space: nowrap; line-height: 1; }
  .label--gold { color: var(--gold); }
  .label--beige { color: var(--beige); }
  .circle-label { font-size: 27px; text-align: center; }
  .circle-label--right { font-size: 21px; line-height: 1.25; white-space: normal; width: 160px; }
  .answer { font-size: 28px; }
  .answer--small { font-size: 20px; }
  .product { font-size: 28px; }
  .bubble-text {
    position: absolute;
    left: 628px; top: 90px;
    width: 175px;
    font-size: 15px;
    line-height: 1.2;
    color: var(--bubble-text);
  }
  .hand-with-money {
    position: absolute;
    left: 470px; top: 868px;
    width: 180px; height: 105px;
    border-radius: 30px;
    background: linear-gradient(160deg, var(--bubble) 0%, #e9a92a 55%, #2f9a5a 56%, #3aa866 100%);
  }
</style>
</head>
<body>
<main class="canvas">
  <div class="world-map" role="img" aria-label="Faint world map behind the ribbons"></div>

  <svg class="artwork" width="1200" height="1002" viewBox="0 0 1200 1002" aria-hidden="true">
    <!-- ribbons -->
    <g fill="none" stroke="var(--ribbon)" stroke-width="50" stroke-linecap="butt">
      <path class="ribbon ribbon--imported" d="M330,280 L330,345 C330,400 360,420 430,425 C505,430 535,470 535,520 L535,580"/>
      <path class="ribbon ribbon--local" d="M830,280 L830,345 C830,400 800,420 730,425 C655,430 622,470 622,520 L622,590"/>
    </g>
    <circle class="ribbon-head" cx="307" cy="229" r="106" fill="var(--ribbon)"/>
    <circle class="ribbon-head" cx="848" cy="229" r="106" fill="var(--ribbon)"/>

    <!-- speech bubble -->
    <path class="speech-bubble-frame" d="M585,85 Q590,62 640,62 L790,62 Q830,62 832,100 L832,140 Q830,168 800,170 L860,185 L780,195 Q740,215 650,210 Q590,208 585,170 Z" fill="var(--white)"/>
    <path class="speech-bubble" d="M598,92 Q602,74 642,74 L788,74 Q818,74 820,102 L820,138 Q818,160 790,162 L830,180 L776,184 Q740,202 652,198 Q600,196 598,168 Z" fill="var(--bubble)"/>

    <!-- arrows up-left / up-right -->
    <g class="arrow arrow--imported" transform="translate(465,670) rotate(-40)">
      <polygon points="-18,-45 0,-68 18,-45 9,-45 9,-30 -9,-30 -9,-45" fill="var(--ribbon)"/>
      <rect x="-9" y="-30" width="18" height="70" fill="#b85748"/>
      <g fill="none" stroke="var(--ribbon)" stroke-width="4">
        <polyline points="-9,0 0,8 9,0"/><polyline points="-9,12 0,20 9,12"/><polyline points="-9,24 0,32 9,24"/>
      </g>
    </g>
    <g class="arrow arrow--local" transform="translate(700,670) rotate(40)">
      <polygon points="-18,-45 0,-68 18,-45 9,-45 9,-30 -9,-30 -9,-45" fill="var(--ribbon)"/>
      <rect x="-9" y="-30" width="18" height="70" fill="#b85748"/>
      <g fill="none" stroke="var(--ribbon)" stroke-width="4">
        <polyline points="-9,0 0,8 9,0"/><polyline points="-9,12 0,20 9,12"/><polyline points="-9,24 0,32 9,24"/>
      </g>
    </g>

    <!-- growth chart icon -->
    <g class="growth-chart" fill="var(--beige)">
      <rect x="512" y="798" width="18" height="18" rx="8"/>
      <rect x="537" y="780" width="18" height="36" rx="8"/>
      <rect x="562" y="758" width="18" height="58" rx="8"/>
      <rect x="587" y="733" width="18" height="83" rx="8"/>
      <path d="M515,770 Q560,745 598,700" fill="none" stroke="var(--beige)" stroke-width="9" stroke-linecap="round"/>
      <polygon points="584,690 616,680 606,712"/>
    </g>
  </svg>

  <span class="label label--gold circle-label" style="left:242px;top:218px;">Absolutely</span>
  <span class="label label--gold circle-label circle-label--right" style="left:769px;top:195px;">Not<br>on Australia's<br>watch</span>

  <span class="label label--beige answer--small" style="left:445px;top:229px;">Free trade over Free Health</span>
  <span class="label label--beige answer" style="left:380px;top:336px;">NO</span>
  <span class="label label--beige answer--small" style="left:488px;top:341px;">&lt;=organic=&gt;</span>
  <span class="label label--beige answer" style="left:658px;top:336px;">Hopefully</span>
  <span class="label label--beige answer" style="left:224px;top:469px;">Questionable</span>
  <span class="label label--beige answer" style="left:763px;top:469px;">Most definatley</span>

  <span class="label label--gold product" style="left:238px;top:560px;">Berries - imported</span>
  <span class="label label--gold product" style="left:697px;top:560px;">Berries- local</span>

  <p class="bubble-text">I know we cost more, but do you think people will get it yet?</p>

  <div class="hand-with-money" role="img" aria-label="Hand holding out a dollar banknote"></div>
</main>
</body>
</html>
```